Vextara website

Web design for small consulting firm
It can be simple, easy to find approach

The primary use is business to business for

a. people wanting to find out a bit more of us after receiving a business card
b. Search words to draw people from search engines to us

Target Market(s)

Senior staff of large companies, in their work capacity
MD / CEO / CFO , directors, etc.

Industry/Entity Type

Business

Colors
ffffff
f79020
faa54b
33a6d7

```html
<!DOCTYPE html>
<html lang="en">
<head>
<meta charset="utf-8">
<title>Vextara — Consulting</title>
<link rel="stylesheet" href="https://fonts.googleapis.com/css2?family=Open+Sans:wght@400;600;700&family=Ubuntu:wght@400;500&display=swap">
<style>
:root{
  --white:#ffffff;
  --orange:#f79020;
  --orange-light:#faa54b;
  --blue:#33a6d7;
  --navy:#1d4f91;
  --ink:#222;
  --grey:#666;
  --hero-top:#0e0e10;
  --hero-bottom:#4a4d57;
  --panel:#eef1f4;
  --panel-dark:#d8dee4;
  --footer-top:#3b3b3b;
  --footer-bottom:#1f1f1f;
  --btn-dark:#3a3a3a;
}
*{box-sizing:border-box;margin:0;padding:0}
html,body{width:686px;height:1200px;overflow:hidden;background:var(--white)}
body{position:relative;font-family:'Open Sans',Arial,sans-serif;color:var(--ink)}
.abs{position:absolute}

/* Header */
.site-header{position:absolute;left:0;top:0;width:686px;height:66px;background:var(--white);border-top:3px solid var(--orange)}
.brand{position:absolute;left:100px;top:16px;display:flex;align-items:center;gap:6px;font-family:'Ubuntu',sans-serif;font-weight:500;font-size:24px;color:var(--blue)}
.brand-dot{width:12px;height:12px;border-radius:50%;background:var(--orange)}
.main-nav a{position:absolute;top:0;height:63px;line-height:70px;font-size:8px;color:var(--ink);text-decoration:none}
.main-nav a.active{background:var(--blue);color:var(--white);width:36px;text-align:center}

/* Hero */
.hero{position:absolute;left:0;top:66px;width:686px;height:276px;background:linear-gradient(var(--hero-top),var(--hero-bottom))}
.hero-title{position:absolute;left:105px;top:60px;color:var(--white);font-size:13px;font-weight:400}
.hero-list{position:absolute;left:106px;top:86px;list-style:none}
.hero-list li{color:var(--white);font-size:10px;height:22.5px;display:flex;align-items:center;gap:6px}
.tick{width:8px;height:8px;flex:none}
.btn-start{position:absolute;left:105px;top:204px;width:110px;height:29px;background:#334866;color:var(--white);font-size:11px;line-height:29px;text-align:center;border-radius:2px}
.laptop{position:absolute;left:304px;top:60px}
.pager{position:absolute;left:294px;top:250px;width:90px;height:14px;background:#eee;border-radius:2px}

/* Feature band */
.feature-band{position:absolute;left:0;top:342px;width:686px;height:133px;background:linear-gradient(var(--orange),var(--orange-light) 50%,var(--orange))}
.feature-card{position:absolute;top:16px;width:118px;height:97px;background:var(--white);border:1px solid #f3d2a8}
.feature-art{position:absolute;left:0;top:0;width:116px;height:71px;background:radial-gradient(circle,#f1c04a 0,#e9d7a8 35%,#fff 70%)}
.feature-label{position:absolute;left:0;bottom:0;width:116px;height:24px;background:linear-gradient(#45b1e0,var(--blue));color:var(--white);font-size:10px;line-height:24px;text-align:center}

/* Articles */
.articles{position:absolute;left:0;top:475px;width:686px;height:213px;background:linear-gradient(#f6f8fa,var(--panel));border-bottom:1px solid #d6dbe0}
.section-title{font-size:13px;font-weight:600;color:var(--navy)}
.articles .section-title{position:absolute;left:100px;top:27px}
.articles-intro{position:absolute;left:101px;top:50px;font-size:6.6px;color:var(--navy)}
.articles-list{position:absolute;left:101px;top:67px;list-style:none}
.articles-list li{font-family:Arial,sans-serif;font-size:6.5px;color:var(--grey);height:19.6px;display:flex;align-items:center;gap:5px}
.btn-dark{position:absolute;background:linear-gradient(#4a4a4a,#2a2a2a);color:var(--white);font-size:7.5px;font-weight:600;text-align:center;border-radius:2px}
.tablet{position:absolute;left:444px;top:16px;width:130px;height:169px;background:var(--white);border:1px solid #ccc;border-radius:5px;box-shadow:0 1px 3px rgba(0,0,0,.2)}
.tablet-art{position:absolute;left:13px;top:14px;width:104px;height:140px;background:linear-gradient(135deg,#fff,#f4e4b8 55%,#e8b93f)}

/* Welcome */
.welcome{position:absolute;left:0;top:688px;width:686px;height:150px;background:var(--white);border-bottom:1px solid #cfd4d9}
.devices-art{position:absolute;left:124px;top:22px;width:160px;height:106px;background:linear-gradient(#9a9a9a,#cfcfcf);border-radius:3px}
.welcome .section-title{position:absolute;left:322px;top:21px;font-size:11px}
.welcome-text{position:absolute;left:324px;top:40px;font-size:7.4px;line-height:14.3px;color:var(--ink)}

/* Contact */
.contact{position:absolute;left:0;top:838px;width:686px;height:246px;background:linear-gradient(var(--panel),var(--panel-dark))}
.contact-title{position:absolute;left:0;top:23px;width:686px;text-align:center;font-size:19px;font-weight:600;letter-spacing:1.5px;color:var(--ink)}
.field{position:absolute;left:137px;width:203px;background:var(--white);border:1px solid #aab;font-size:8px;color:#333;padding:9px 12px}
.btn-send{position:absolute;left:136px;top:199px;width:78px;height:27px;background:var(--orange);color:var(--white);font-size:8.5px;font-weight:600;line-height:27px;text-align:center}
.contact-info{position:absolute;left:368px;top:70px;font-size:10px;font-weight:600;line-height:14px;color:var(--ink)}
.contact-phone{position:absolute;left:368px;top:114px;font-size:10px;font-weight:600;line-height:15px}

/* Footer */
.site-footer{position:absolute;left:0;top:1084px;width:686px;height:116px;background:linear-gradient(var(--footer-top),var(--footer-bottom))}
.footer-links{position:absolute;left:0;top:18px;width:686px;text-align:center;font-size:7px;color:var(--white)}
.footer-links span{margin:0 4px}
.copyright{position:absolute;left:0;top:80px;width:686px;text-align:center;font-size:7px;color:var(--white)}
</style>
</head>
<body>

<header class="site-header">
  <div class="brand"><span class="brand-dot"></span>Vextara</div>
  <nav class="main-nav">
    <a class="active" style="left:351px">HOME</a>
    <a style="left:395px">ABOUT US</a>
    <a style="left:446px">SERVICE</a>
    <a style="left:488px">USEFUL LINKS</a>
    <a style="left:553px">CONTACT</a>
  </nav>
</header>

<section class="hero">
  <h2 class="hero-title">TALK TO US ABOUT</h2>
  <ul class="hero-list">
    <li><svg class="tick" viewBox="0 0 10 10"><circle cx="5" cy="5" r="5" fill="#33a6d7"/><path d="M2.6 5.2l1.6 1.6 3.2-3.4" stroke="#fff" stroke-width="1.4" fill="none"/></svg>Governance</li>
    <li><svg class="tick" viewBox="0 0 10 10"><circle cx="5" cy="5" r="5" fill="#33a6d7"/><path d="M2.6 5.2l1.6 1.6 3.2-3.4" stroke="#fff" stroke-width="1.4" fill="none"/></svg>Good Stewardship</li>
    <li><svg class="tick" viewBox="0 0 10 10"><circle cx="5" cy="5" r="5" fill="#33a6d7"/><path d="M2.6 5.2l1.6 1.6 3.2-3.4" stroke="#fff" stroke-width="1.4" fill="none"/></svg>Financial Management Insight</li>
    <li><svg class="tick" viewBox="0 0 10 10"><circle cx="5" cy="5" r="5" fill="#33a6d7"/><path d="M2.6 5.2l1.6 1.6 3.2-3.4" stroke="#fff" stroke-width="1.4" fill="none"/></svg>Information Technology Insight</li>
    <li><svg class="tick" viewBox="0 0 10 10"><circle cx="5" cy="5" r="5" fill="#33a6d7"/><path d="M2.6 5.2l1.6 1.6 3.2-3.4" stroke="#fff" stroke-width="1.4" fill="none"/></svg>Mentoring and Business Advice</li>
  </ul>
  <div class="btn-start">GET START NOW</div>

  <svg class="laptop" width="282" height="152" viewBox="0 0 282 152">
    <rect x="36" y="0" width="211" height="140" rx="5" fill="#1a1a1a" stroke="#bbb" stroke-width="1.5"/>
    <rect x="44" y="9" width="195" height="122" fill="#ee7a1c" role="img" aria-label="Video still: hands on an orange surface"/>
    <circle cx="143" cy="70" r="14" fill="rgba(60,40,20,.75)"/>
    <path d="M139 63l11 7-11 7z" fill="#fff"/>
    <rect x="0" y="140" width="282" height="8" rx="2" fill="#d9d9d9"/>
    <rect x="8" y="148" width="266" height="3" rx="1.5" fill="#999"/>
  </svg>

  <svg class="pager" viewBox="0 0 90 14">
    <rect width="90" height="14" rx="2" fill="#eee"/>
    <path d="M9 5l-2 2 2 2M15 5l2 2-2 2" stroke="#333" stroke-width="1.2" fill="none"/>
    <line x1="26" y1="2" x2="26" y2="12" stroke="#ccc"/>
    <circle cx="34" cy="7" r="2" fill="#aaa"/><circle cx="43" cy="7" r="2" fill="#aaa"/>
    <circle cx="52" cy="7" r="2" fill="#333"/><circle cx="61" cy="7" r="2" fill="#aaa"/>
    <circle cx="70" cy="7" r="2" fill="#aaa"/><circle cx="79" cy="7" r="2" fill="#aaa"/>
  </svg>
</section>

<section class="feature-band">
  <div class="feature-card" style="left:98px"><div class="feature-art" role="img" aria-label="Gold figure turning a large key"></div><div class="feature-label">WHO WE ARE</div></div>
  <div class="feature-card" style="left:223px"><div class="feature-art" role="img" aria-label="Gold figure carrying a box"></div><div class="feature-label">OUR VALUES</div></div>
  <div class="feature-card" style="left:347px"><div class="feature-art" role="img" aria-label="Gold figures holding a light bulb"></div><div class="feature-label">WHAT WE DO</div></div>
  <div class="feature-card" style="left:471px"><div class="feature-art" role="img" aria-label="Orange folder with a clock"></div><div class="feature-label">OUR CLIENTS</div></div>
</section>

<section class="articles">
  <h2 class="section-title">ARTICLES AND PUBLICATIONS</h2>
  <p class="articles-intro">So here is the process we want to illustrate, please &nbsp;be creative as this is the bulk of our sales pitch.</p>
  <ul class="articles-list">
    <li><svg class="tick" viewBox="0 0 10 10"><circle cx="5" cy="5" r="5" fill="#f06a2a"/><path d="M2.6 5.2l1.6 1.6 3.2-3.4" stroke="#fff" stroke-width="1.4" fill="none"/></svg>Tell our team your goals and let us customize a roadmap to get your there.</li>
    <li><svg class="tick" viewBox="0 0 10 10"><circle cx="5" cy="5" r="5" fill="#f06a2a"/><path d="M2.6 5.2l1.6 1.6 3.2-3.4" stroke="#fff" stroke-width="1.4" fill="none"/></svg>Start any course for free 3. If you like the course continue by only paying what you feel</li>
    <li><svg class="tick" viewBox="0 0 10 10"><circle cx="5" cy="5" r="5" fill="#f06a2a"/><path d="M2.6 5.2l1.6 1.6 3.2-3.4" stroke="#fff" stroke-width="1.4" fill="none"/></svg>If you run into issues, contact the teacher directly and work one-on-one until you feel comfortable</li>
    <li><svg class="tick" viewBox="0 0 10 10"><circle cx="5" cy="5" r="5" fill="#f06a2a"/><path d="M2.6 5.2l1.6 1.6 3.2-3.4" stroke="#fff" stroke-width="1.4" fill="none"/></svg>Pay teachers for one-on-one sessions with our secure escrow system</li>
    <li><svg class="tick" viewBox="0 0 10 10"><circle cx="5" cy="5" r="5" fill="#f06a2a"/><path d="M2.6 5.2l1.6 1.6 3.2-3.4" stroke="#fff" stroke-width="1.4" fill="none"/></svg>Stay up to date on our blog with REAL industry expert contributors</li>
  </ul>
  <div class="btn-dark" style="left:100px;top:166px;width:68px;height:20px;line-height:20px">VIEW MORE</div>
  <div class="tablet">
    <div class="tablet-art" role="img" aria-label="Gold figure ticking a checklist with a large pen"></div>
    <svg class="abs" style="left:55px;top:71px" width="30" height="30" viewBox="0 0 30 30"><circle cx="15" cy="15" r="13" fill="rgba(60,40,20,.7)"/><path d="M12 9l9 6-9 6z" fill="#fff"/></svg>
  </div>
</section>

<section class="welcome">
  <div class="devices-art" role="img" aria-label="Desktop, laptop, tablet and phone showing the site"></div>
  <h2 class="section-title">WELCOME TO VEXTARA</h2>
  <p class="welcome-text">This page will be for us to communicate our specific capture points.<br>This will be set up for mostly skimming and no long length of text.<br>You can lay a design and lorem the text and we'll take care of it later<br>Cater for about points to be made</p>
  <div class="btn-dark" style="left:324px;top:106px;width:69px;height:19px;line-height:19px">VIEW MORE</div>
</section>

<section class="contact">
  <h2 class="contact-title">GET IN TOUCH</h2>
  <div class="field" style="top:74px;height:28px">Your Name</div>
  <div class="field" style="top:116px;height:28px">Your Email</div>
  <div class="field" style="top:159px;height:35px">Your Message</div>
  <div class="btn-send">SEND</div>
  <p class="contact-info">Vextara Advisory Limited &nbsp;PO Box 40215<br>&nbsp;Harbourside &nbsp;6011</p>
  <p class="contact-phone">T: &nbsp;021 555 0187<br>M: &nbsp;021 555 0187</p>
  <svg class="abs" style="left:367px;top:168px" width="122" height="32" viewBox="0 0 122 32">
    <circle cx="16" cy="16" r="14.5" fill="none" stroke="#777"/>
    <circle cx="60" cy="16" r="14.5" fill="none" stroke="#777"/>
    <circle cx="104" cy="16" r="14.5" fill="none" stroke="#777"/>
  </svg>
</section>

<footer class="site-footer">
  <p class="footer-links">About Us<span>|</span>Advertise With Us<span>|</span>FAQ<span>|</span>Terms and Conditions<span>|</span>Privacy Policy<span>|</span>Contact Us</p>
  <svg class="abs" style="left:274px;top:47px" width="138" height="22" viewBox="0 0 138 22">
    <circle cx="11" cy="11" r="10" fill="#eee"/><circle cx="34" cy="11" r="10" fill="#eee"/>
    <circle cx="57" cy="11" r="10" fill="#eee"/><circle cx="80" cy="11" r="10" fill="#eee"/>
    <circle cx="103" cy="11" r="10" fill="#eee"/><circle cx="126" cy="11" r="10" fill="#eee"/>
  </svg>
  <p class="copyright">Copyright © 2012 . All Rights Reserved.</p>
</footer>

</body>
</html>
```